modernized upgrade to existing squarespace site

Hello! I have the following page for my consulting firm: https://fernwaystrategygroup.com/ Would love to upgrade to something more modern/attractive like here: https://www.lobrettiandco.com/ or https://quillbrightlab.com/ , but I am open to creativity. Would like to retain the logo look and color theme from the logo. The rest can be left to creative discretion.

```html
<!DOCTYPE html>
<html lang="en">
<head>
<meta charset="utf-8">
<title>Fernway Strategy Group</title>
<link rel="stylesheet" href="https://fonts.googleapis.com/css2?family=Cinzel:wght@400;500&family=Poppins:ital,wght@0,400;0,500;0,600;1,500&display=swap">
<style>
:root{
  --ink:#1c1a1a;
  --ink-soft:#2a2624;
  --rose:#c98e84;
  --rose-faint:#f1e4e1;
  --paper:#f6f5f5;
  --white:#ffffff;
  --text:#2b2b2b;
  --muted:#6b6b6b;
}
*{margin:0;padding:0;box-sizing:border-box}
html,body{width:1200px;height:5128px;overflow:hidden}
body{position:relative;background:var(--paper);font-family:'Poppins',sans-serif;color:var(--text)}
.abs{position:absolute}

/* hero */
.hero{left:0;top:0;width:1200px;height:718px;background:var(--ink);overflow:hidden}
.brand{display:flex;align-items:center;gap:14px}
.brand-mark{width:52px;height:52px;border:2px solid var(--rose)}
.brand-name{font-family:'Cinzel',serif;font-weight:400;color:var(--white);font-size:22px;letter-spacing:3px;line-height:1.2}
.nav{left:440px;top:46px;display:flex;gap:24px;font-size:15px;color:var(--white)}
.nav .active{color:var(--rose)}
.btn-outline{border:2px solid var(--white);color:var(--white);font-size:15px;letter-spacing:1px;display:flex;align-items:center;justify-content:center}
.hero-eyebrow{left:110px;top:200px;font-family:'Cinzel',serif;color:var(--rose);font-size:21px}
.hero-title{left:110px;top:248px;white-space:nowrap;color:var(--white);font-weight:600;font-size:46px;line-height:1.28}
.hero-photo{left:557px;top:138px;width:530px;height:507px;border:3px solid var(--rose);background:linear-gradient(160deg,#9aa0a6 0%,#6e6a66 45%,#5a3c30 80%,#2c2420 100%)}
.hero-ghost{left:0;top:560px;font-weight:600;font-size:170px;letter-spacing:14px;color:#3b2a26;line-height:1}
.social-dot{left:1155px;top:322px;width:40px;height:40px;border-radius:50%;background:#3a3634}

/* press */
.press-label{left:0;width:1200px;top:780px;text-align:center;font-weight:500;font-size:20px}
.badge{width:227px;height:108px;background:var(--white);box-shadow:0 2px 8px rgba(0,0,0,.06);display:flex;align-items:center;justify-content:center}
.badge span{width:110px;height:56px;background:#d9d6d5}

/* section heads */
.sec-title{font-family:'Cinzel',serif;font-size:42px;color:var(--ink);line-height:1.35;white-space:nowrap}
.rule{height:3px;background:var(--rose)}
.ghost{font-weight:600;color:var(--rose-faint);letter-spacing:18px;line-height:1}

/* about */
.about-photo{left:0;top:1225px;width:730px;height:600px;background:linear-gradient(135deg,#b9b3ad,#e6e2de 55%,#8c7f78)}
.welcome{left:787px;top:1214px;width:413px}
.welcome .sec-title{font-size:36px;line-height:1.3}
.welcome .rule{margin-top:10px;width:413px}
.card{background:var(--white);box-shadow:0 2px 14px rgba(0,0,0,.05)}
.about-card{left:622px;top:1470px;width:466px;height:502px;padding:42px 40px}
.card-lead{font-weight:500;font-size:20px;line-height:1.55;color:var(--ink);margin-bottom:30px}
.card-body{font-size:15px;line-height:1.93;color:var(--muted);margin-bottom:28px}

/* services */
.svc{width:310px;height:497px;top:2313px;background:var(--white)}
.svc-photo{height:227px}
.svc h3{font-weight:500;font-size:21px;margin:40px 22px 16px;color:var(--ink)}
.svc p{font-size:15px;line-height:1.85;color:var(--muted);margin:0 22px}

/* research */
.research-photo{left:0;top:2905px;width:730px;height:676px;background:linear-gradient(120deg,#3c4446,#6e7577 50%,#2a2f30)}
.research-band{left:0;top:2905px;width:215px;height:676px;background:var(--ink-soft)}
.research-vert{left:40px;top:3581px;transform-origin:0 0;transform:rotate(-90deg);font-weight:600;font-size:110px;letter-spacing:10px;color:var(--rose);line-height:1;white-space:nowrap}
.research-card{left:597px;top:3122px;width:492px;height:358px;padding:52px 50px}
.research-card p{font-weight:500;font-size:25px;line-height:1.72;color:var(--ink)}
.btn-dark{border:2px solid var(--ink);color:var(--ink);font-size:17px;width:126px;height:52px;display:flex;align-items:center;justify-content:center;margin-top:26px}

/* news */
.news-photo{left:141px;top:3850px;width:404px;height:410px;background:linear-gradient(140deg,#bcd0da,#8fb3c6 50%,#dde8ee)}
.news-quote{left:545px;top:3850px;width:514px;height:410px;background:var(--rose);padding:55px 50px;color:var(--white)}
.news-quote blockquote{font-style:italic;font-weight:500;font-size:26px;line-height:1.5}
.news-quote cite{display:block;font-style:normal;font-size:16px;margin-top:36px;opacity:.9}
.dots{left:0;width:1200px;top:4314px;display:flex;justify-content:center;gap:8px}
.dots i{width:10px;height:10px;border-radius:50%;border:1.5px solid #8a8a8a}
.dots i.on{background:#8a8a8a}

/* footer */
.footer{left:0;top:4515px;width:1200px;height:613px;background:var(--ink)}
.news-card{left:110px;top:4405px;width:979px;height:265px;background:var(--white)}
.news-card h2{position:absolute;left:93px;top:40px;font-weight:600;font-size:29px;color:var(--ink)}
.news-card .rule{position:absolute;left:0;top:90px;width:515px}
.news-card p{position:absolute;left:93px;top:117px;font-size:15px;color:var(--muted)}
.field{position:absolute;left:93px;top:170px;width:650px;height:54px;background:#f2f1f1;font-size:15px;display:flex;align-items:center;padding-left:24px;color:#444}
.signup{position:absolute;left:743px;top:170px;width:115px;height:54px;background:var(--ink);color:var(--white);font-weight:600;font-size:15px;display:flex;align-items:center;justify-content:center}
.foot-head{font-weight:600;font-size:18px;color:var(--white)}
.foot-list{list-style:none;font-size:15px;line-height:1.84;color:var(--white)}
.foot-row{display:flex;gap:18px;font-size:15px;color:var(--white);line-height:1.7}
.foot-rule{left:110px;top:5015px;width:979px;height:1px;background:#4a4644}
.copy{left:0;width:1200px;top:5060px;text-align:center;font-size:15px;color:var(--white)}
</style>
</head>
<body>

<!-- Hero -->
<section class="abs hero">
  <div class="abs brand" style="left:110px;top:26px">
    <div class="brand-mark"></div>
    <div class="brand-name">FERNWAY<br>STRATEGY GROUP</div>
  </div>
  <nav class="abs nav">
    <span class="active">Home</span><span>Services</span><span>Research</span><span>The Institute</span><span>In the News</span>
  </nav>
  <div class="abs btn-outline" style="left:965px;top:32px;width:125px;height:52px">CONTACT</div>
  <p class="abs hero-eyebrow">Fernway Strategy Group</p>
  <h1 class="abs hero-title">Macroeconomic<br>&amp; policy<br>analytics for<br>today’s turbulent<br>environment</h1>
  <div class="abs hero-ghost">FERNWAY</div>
  <div class="abs hero-photo" role="img" aria-label="Photo of city office buildings under a grey sky"></div>
  <div class="abs social-dot"></div>
</section>

<!-- Press -->
<p class="abs press-label">As seen on</p>
<div class="abs badge" style="left:110px;top:860px"><span></span></div>
<div class="abs badge" style="left:360px;top:860px"><span></span></div>
<div class="abs badge" style="left:611px;top:860px"><span></span></div>
<div class="abs badge" style="left:862px;top:860px"><span></span></div>
<div class="abs badge" style="left:236px;top:990px"><span></span></div>
<div class="abs badge" style="left:486px;top:990px"><span></span></div>
<div class="abs badge" style="left:737px;top:990px"><span></span></div>

<!-- About -->
<div class="abs about-photo" role="img" aria-label="Photo of hands reviewing printed charts and reports on a desk"></div>
<div class="abs welcome">
  <h2 class="sec-title">WELCOME TO<br>FERNWAY<br>STRATEGY GROUP</h2>
  <div class="rule"></div>
</div>
<div class="abs ghost" style="left:0;top:1855px;font-size:120px;color:#efe5e3">ABOUT</div>
<div class="abs card about-card">
  <p class="card-lead">Thoughtful solutions that bridge the academic with private industry.</p>
  <p class="card-body">The Fernway Policy Institute (FPI) is an independent non-profit organization that partners with private think tanks, academic institutions, and policy advocacy organizations to develop unbiased investigations and reasoned responses to the macroeconomic policy concerns of today.</p>
  <p class="card-body">Please see below for a growing list of current partners, support organizations, and affiliated institutions, along with a preview of some of our recent work.</p>
</div>

<!-- Services -->
<div class="abs ghost" style="left:468px;top:2150px;font-size:110px">SERVICES</div>
<h2 class="abs sec-title" style="left:110px;top:2170px">WHAT WE DO</h2>
<div class="abs rule" style="left:0;top:2250px;width:398px"></div>
<article class="abs svc" style="left:110px">
  <div class="svc-photo" role="img" aria-label="Photo of a colleague presenting a colour-coded chart" style="background:linear-gradient(135deg,#d8d2c8,#f2ede6 60%,#b9a894)"></div>
  <h3>Analytics &amp; Messaging</h3>
  <p>Our communications team can develop influential messaging, in conjunction with our data scientists’ technical expertise.</p>
</article>
<article class="abs svc" style="left:446px">
  <div class="svc-photo" role="img" aria-label="Photo of an analyst working at a desktop monitor showing charts" style="background:linear-gradient(135deg,#3a3330,#cfcac4 55%,#efece8)"></div>
  <h3>Customized Reports</h3>
  <p>From succinct summations of economic and policy impact to full-length analyses, we can create the customized exposition that best represents your interests.</p>
</article>
<article class="abs svc" style="left:779px">
  <div class="svc-photo" role="img" aria-label="Photo of three colleagues reviewing documents together" style="background:linear-gradient(135deg,#e7e4e0,#b58866 50%,#d9d4cf)"></div>
  <h3>Proprietary Surveys</h3>
  <p>Exclusive, custom-designed surveys can enrich your databank, while maintaining access to proprietary resources, establishing you and your firm as a thought leader.</p>
</article>

<!-- Research -->
<div class="abs research-photo" role="img" aria-label="Photo of hands typing on a laptop displaying a trend chart"></div>
<div class="abs research-band"></div>
<div class="abs research-vert">RESEARCH</div>
<h2 class="abs sec-title" style="left:787px;top:2960px">RESEARCH</h2>
<div class="abs rule" style="left:790px;top:3043px;width:410px"></div>
<div class="abs card research-card">
  <p>Our research spans multiple industries, with a focus on the impact of policy proposals on your company’s future.</p>
  <div class="btn-dark">CONTACT</div>
</div>

<!-- In the news -->
<div class="abs ghost" style="left:520px;top:3672px;font-size:110px">UPDATES</div>
<h2 class="abs sec-title" style="left:110px;top:3694px">IN THE NEWS</h2>
<div class="abs rule" style="left:0;top:3773px;width:398px"></div>
<div class="abs news-photo" role="img" aria-label="Photo of two lab workers in protective caps and masks"></div>
<div class="abs news-quote">
  <blockquote>“. . . commissioned the new economic research report by Fernway Strategy Group to study the industry’s . . . economic impact on&nbsp;states&nbsp;.&nbsp;.&nbsp;”</blockquote>
  <cite>— Clinical Supply Review magazine</cite>
</div>
<div class="abs dots"><i class="on"></i><i></i><i></i><i></i></div>

<!-- Footer -->
<footer class="abs footer">
  <div class="abs brand" style="left:110px;top:280px">
    <div class="brand-mark" style="width:92px;height:92px"></div>
    <div class="brand-name" style="font-size:30px">FERNWAY<br>STRATEGY GROUP</div>
  </div>
  <div class="abs" style="left:578px;top:230px">
    <p class="foot-head">Quick Links</p>
    <ul class="foot-list" style="margin-top:30px">
      <li>Home</li><li>Services</li><li>Research</li><li>The Institute</li><li>In the News</li><li>Contact</li>
    </ul>
  </div>
  <div class="abs" style="left:793px;top:230px">
    <p class="foot-head">Contact Information</p>
    <div class="foot-row" style="margin-top:30px">
      <svg width="14" height="18" viewBox="0 0 14 18"><path d="M7 0a7 7 0 0 0-7 7c0 5 7 11 7 11s7-6 7-11a7 7 0 0 0-7-7zm0 9.5A2.5 2.5 0 1 1 7 4.5a2.5 2.5 0 0 1 0 5z" fill="#fff"/></svg>
      <span>418 Larkspur Ave, Suite 210,<br>Alder City, 40112</span>
    </div>
    <div class="foot-row" style="margin-top:20px;align-items:center">
      <svg width="16" height="12" viewBox="0 0 16 12"><rect width="16" height="12" rx="1" fill="#fff"/><path d="M1 1l7 5 7-5" stroke="#1c1a1a" stroke-width="1.4" fill="none"/></svg>
      <span>info@FernwayStrategy.com</span>
    </div>
  </div>
</footer>
<div class="abs foot-rule"></div>
<p class="abs copy">Fernway Strategy Group © 2024. All rights reserved.</p>

<!-- Newsletter -->
<div class="abs news-card">
  <h2>Subscribe to Our Newsletter</h2>
  <div class="rule"></div>
  <p>Sign up with your email address to receive news and updates.</p>
  <div class="field">Email Address</div>
  <div class="signup">SIGN UP</div>
</div>

</body>
</html>
```